TRV business card

Need a business card for a company that provides instructional design and elearning development services. The website is here: http://tarvexa.studio/

I'm attaching a current logo, as well as the old business card design. While I like to keep it clean, the old design is too simplistic for my liking. The only idea I want to reuse from the old design is placing industry jargon on the back of the card, just need a better way to present it. But if you have other ideas for the back--feel free to experiment.

Please use the colors complementary to the color we have on the website. Thank you!

```html
<!DOCTYPE html>
<html lang="en">
<head>
<meta charset="utf-8">
<title>TRV business card</title>
<link href="https://fonts.googleapis.com/css2?family=Open+Sans:wght@400;600;700&display=swap" rel="stylesheet">
<style>
  :root {
    --bg: #e7e4df;
    --teal: #17b1ad;
    --teal-dark: #13a3a0;
    --gold: #e2d59c;
    --sage: #b7bd85;
    --ink: #2a2a2a;
    --card-dark: #232323;
    --white: #ffffff;
    --faint: #f2f2f2;
  }
  * { box-sizing: border-box; margin: 0; padding: 0; }
  html, body { width: 1200px; height: 1000px; overflow: hidden; }
  body {
    position: relative;
    background: var(--bg);
    font-family: "Open Sans", sans-serif;
  }
  .card {
    position: absolute;
    left: 265px;
    width: 665px;
    height: 397px;
    border-radius: 22px;
    overflow: hidden;
    box-shadow: 0 6px 18px rgba(0,0,0,0.18);
  }
  .card--front { top: 73px; background: var(--white); }
  .card--back { top: 533px; background: var(--card-dark); }

  .brand { position: absolute; display: flex; align-items: center; }
  .brand__mark { border-radius: 50%; background: var(--teal); flex: none; }
  .brand__name { font-weight: 700; color: var(--gold); letter-spacing: 2px; line-height: 1; }

  .card--front .brand { left: 32px; top: 50px; gap: 16px; }
  .card--front .brand__mark { width: 58px; height: 58px; }
  .card--front .brand__name { font-size: 54px; }

  .front__watermark {
    position: absolute; right: 34px; top: 150px;
    font-weight: 700; font-size: 150px; color: var(--faint);
    letter-spacing: 6px; line-height: 1;
  }

  .holder {
    position: absolute; left: 33px; top: 214px;
    font-size: 20px; font-weight: 700; color: var(--teal);
  }
  .contacts { position: absolute; left: 33px; top: 266px; list-style: none; }
  .contacts__item {
    display: flex; align-items: center; gap: 7px;
    font-size: 16.5px; color: var(--ink); height: 25.5px;
  }
  .contacts__icon { width: 15px; height: 15px; fill: var(--teal); flex: none; }

  .front__band { position: absolute; left: 0; bottom: 0; width: 665px; height: 34px; }

  .card--back .brand { left: 0; right: 0; top: 62px; justify-content: center; gap: 18px; }
  .card--back .brand__mark { width: 62px; height: 62px; }
  .card--back .brand__name { font-size: 60px; }

  .services {
    position: absolute; left: 40px; top: 214px; width: 565px;
    display: flex; justify-content: space-between; list-style: none;
  }
  .service { width: 140px; display: flex; flex-direction: column; align-items: center; }
  .service__badge {
    width: 84px; height: 84px; border-radius: 50%;
    border: 2px solid var(--gold);
    display: flex; align-items: center; justify-content: center;
  }
  .service__icon { width: 36px; height: 36px; fill: var(--gold); }
  .service__label {
    margin-top: 18px; text-align: center; color: var(--white);
    font-size: 16.5px; line-height: 22px; text-transform: uppercase;
  }
</style>
</head>
<body>

  <section class="card card--front">
    <div class="brand">
      <span class="brand__mark"></span>
      <span class="brand__name">TRV</span>
    </div>
    <div class="front__watermark" aria-hidden="true">TRV</div>

    <h1 class="holder">Marina Castell</h1>
    <ul class="contacts">
      <li class="contacts__item">
        <svg class="contacts__icon" viewBox="0 0 16 16"><path d="M2 5c0-2 2-3 6-3s6 1 6 3v1h-3V5H5v1H2z M4 7h8l2 6H2z M8 9a1.5 1.5 0 1 0 0 3a1.5 1.5 0 0 0 0-3z"/></svg>
        555-014-2287
      </li>
      <li class="contacts__item">
        <svg class="contacts__icon" viewBox="0 0 16 16"><path d="M1 3h14v10H1z M2 4l6 5l6-5" stroke="#fff" stroke-width="1.2"/></svg>
        mcastell@tarvexa.studio
      </li>
      <li class="contacts__item">
        <svg class="contacts__icon" viewBox="0 0 16 16"><circle cx="8" cy="8" r="7"/><path d="M1 8h14M8 1c3 3 3 11 0 14M8 1c-3 3-3 11 0 14" stroke="#fff" stroke-width="1" fill="none"/></svg>
        www.tarvexa.studio
      </li>
    </ul>

    <svg class="front__band" viewBox="0 0 665 34" preserveAspectRatio="none" aria-hidden="true">
      <defs>
        <linearGradient id="bandGrad" x1="0" x2="1" y1="0" y2="0">
          <stop offset="0" stop-color="#c6bd83"/>
          <stop offset="0.55" stop-color="#b9c48f"/>
          <stop offset="1" stop-color="#2fb6ad"/>
        </linearGradient>
      </defs>
      <rect x="0" y="16" width="665" height="18" fill="var(--teal)"/>
      <path d="M322 34 C350 20 370 2 420 0 L665 0 L665 34 Z" fill="#ffffff"/>
      <path d="M330 34 C356 22 376 5 422 3 L665 3 L665 34 Z" fill="url(#bandGrad)"/>
    </svg>
  </section>

  <section class="card card--back">
    <div class="brand">
      <span class="brand__mark"></span>
      <span class="brand__name">TRV</span>
    </div>

    <ul class="services">
      <li class="service">
        <span class="service__badge">
          <svg class="service__icon" viewBox="0 0 32 32"><path d="M4 10h7a3 3 0 1 1 6 0h7v6a3 3 0 1 1 0 6v6h-7a3 3 0 1 0-6 0H4v-7a3 3 0 1 0 0-6z"/></svg>
        </span>
        <span class="service__label">Instructional<br>Design</span>
      </li>
      <li class="service">
        <span class="service__badge">
          <svg class="service__icon" viewBox="0 0 32 32"><path d="M5 8h18v9a6 6 0 0 1-6 6h-6a6 6 0 0 1-6-6z M23 10h2a4 4 0 0 1 0 8h-2v-3h2a1 1 0 0 0 0-2h-2z M3 25h24v2H3z"/></svg>
        </span>
        <span class="service__label">Elearning<br>Development</span>
      </li>
      <li class="service">
        <span class="service__badge">
          <svg class="service__icon" viewBox="0 0 32 32"><path d="M9 25a7 7 0 0 1-1-14a9 9 0 0 1 17 3a5.5 5.5 0 0 1-1 11z"/><path d="M16 12v9M12 17l4 4l4-4" stroke="#232323" stroke-width="2.4" fill="none"/></svg>
        </span>
        <span class="service__label">Mobile<br>Learning</span>
      </li>
      <li class="service">
        <span class="service__badge">
          <svg class="service__icon" viewBox="0 0 32 32"><path d="M4 10h6l2-3h8l2 3h6v15H4z"/><circle cx="16" cy="17" r="5" fill="#232323"/><circle cx="16" cy="17" r="3"/></svg>
        </span>
        <span class="service__label">Insructor-Led<br>Training</span>
      </li>
    </ul>
  </section>

</body>
</html>
```